Barrowdale Power Loft Chronic Pain Flyer

Double sided DL flyer required to promote a strength training studio to sufferers of chronic pain. Flyer will be displayed in osteopathy, chiropractic and massage clinics. Flyer should be clean, professional and appeal to an older (40+) demographic.

Target Market(s)

Chronic pain sufferers. Age 40+

Industry/Entity Type

Health And Wellness

Colors

Designer to choose colors to be used in the design.

Requirements
Must have
• See attached files for text copy and logo. Image(s) of people strength training with a coach or personal trainer, as well as images depicting pain in common parts of the body (such as those pictured in the supplied mock up)
• website address: barrowdalepowerloft.com.au
• phone number : 0452 918 064
• Street address: 4/83 Kinross Hill Rd, Barrowdale
Nice to have
• Images such as in the attached files.

```html
<!DOCTYPE html>
<html lang="en">
<head>
<meta charset="utf-8">
<title>Barrowdale Power Loft – Chronic Pain Flyer</title>
<link href="https://fonts.googleapis.com/css2?family=Montserrat:wght@500;600;700;800&display=swap" rel="stylesheet">
<style>
:root{
  --bg:#8f8f8f;
  --paper:#ffffff;
  --ink:#5a5a5c;
  --ink-dark:#3f3f42;
  --red:#c8202a;
  --red-soft:#e8888c;
  --plate-a:#ffffff;
  --plate-b:#dedede;
  --band:#58585b;
}
*{box-sizing:border-box;margin:0;padding:0}
html,body{width:1200px;height:1200px;overflow:hidden}
body{background:var(--bg);font-family:"Montserrat",sans-serif;position:relative}
.flyer{position:absolute;top:117px;width:460px;height:966px;background:var(--paper);overflow:hidden;box-shadow:0 6px 18px rgba(0,0,0,.25)}
.flyer--front{left:100px}
.flyer--back{left:640px}
.plate{position:absolute;left:0;right:0;top:250px;height:620px;background:linear-gradient(180deg,var(--plate-a) 0%,var(--plate-b) 45%,var(--plate-a) 100%)}
.brand{position:absolute;top:58px;left:0;right:0;text-align:center;font-weight:800;font-size:27px;letter-spacing:1px;text-transform:uppercase;color:var(--ink)}
.brand-dot{display:inline-block;width:14px;height:14px;border-radius:50%;background:var(--red);margin-right:10px;vertical-align:2px}
.headline{position:absolute;top:140px;left:0;right:0;text-align:center;font-weight:800;text-transform:uppercase;line-height:1}
.headline-top{display:block;font-size:38px;color:var(--ink);letter-spacing:-.5px}
.headline-main{display:block;font-size:68px;color:var(--red);margin-top:4px;letter-spacing:-1px}
.photo{position:absolute;border-radius:50%;border:6px solid var(--red);box-shadow:0 0 0 4px #fff}
.photo-back-pain{left:-20px;top:400px;width:370px;height:370px;background:radial-gradient(circle at 55% 70%,#e06a70 0%,#c9b8b8 30%,#9a9a9a 65%,#d8d8d8 100%)}
.photo-shoulder{left:250px;top:290px;width:300px;height:300px;background:radial-gradient(circle at 30% 35%,#e2747a 0%,#c7b9b9 28%,#8e8e8e 70%,#cfcfcf 100%)}
.photo-knee{left:255px;top:310px;width:300px;height:300px;background:radial-gradient(circle at 45% 50%,#e0666d 0%,#c8b5b5 30%,#8d8d8d 70%,#d2d2d2 100%)}
.tagline{position:absolute;top:280px;left:0;right:0;text-align:center;font-weight:600;font-size:17px;color:var(--ink-dark)}
.body-copy{position:absolute;top:330px;left:34px;width:215px;font-weight:500;font-size:14px;line-height:1.42;color:var(--ink-dark)}
.body-copy p+p{margin-top:14px}
.phone{position:absolute;top:772px;left:0;right:0;display:flex;align-items:center;justify-content:center;gap:12px;font-weight:700;font-size:44px;color:var(--ink)}
.phone svg{width:44px;height:44px}
.band{position:absolute;left:0;right:0;bottom:0;height:118px;background:var(--band);padding:26px 0 0 70px;color:#fff;font-weight:500;font-size:18px}
.band-row{display:flex;align-items:center;gap:10px;margin-bottom:14px}
.band-row svg{width:20px;height:20px;flex:none}
</style>
</head>
<body>

<section class="flyer flyer--front">
  <div class="plate"></div>
  <div class="brand"><span class="brand-dot"></span>Barrowdale Power Loft</div>
  <h1 class="headline"><span class="headline-top">Health Through</span><span class="headline-main">Strength</span></h1>
  <div class="photo photo-back-pain" role="img" aria-label="Black and white photo of a man holding his lower back, painful area glowing red"></div>
  <div class="photo photo-shoulder" role="img" aria-label="Black and white photo of a man holding his shoulder, painful area glowing red"></div>
  <div class="phone">
    <svg viewBox="0 0 44 44"><circle cx="22" cy="22" r="20" fill="#fff" stroke="var(--red)" stroke-width="3"/><path d="M15 13c2-1 3 0 4 2l1 3c0 1-1 2-2 3 1 3 3 5 6 6 1-1 2-2 3-2l3 1c2 1 3 2 2 4-1 2-3 3-5 3-8-1-14-7-15-15 0-2 1-4 3-5z" fill="var(--red)"/></svg>
    <span>0452 918 064</span>
  </div>
  <div class="band">
    <div class="band-row"><svg viewBox="0 0 20 20"><path d="M10 1a6 6 0 0 1 6 6c0 5-6 12-6 12S4 12 4 7a6 6 0 0 1 6-6z" fill="none" stroke="#fff" stroke-width="2"/><circle cx="10" cy="7" r="2" fill="#fff"/></svg>4/83 Kinross Hill Rd, Barrowdale</div>
    <div class="band-row"><svg viewBox="0 0 20 20"><circle cx="10" cy="10" r="8" fill="none" stroke="#fff" stroke-width="2"/><path d="M2 10h16M10 2c3 3 3 13 0 16M10 2c-3 3-3 13 0 16" fill="none" stroke="#fff" stroke-width="1.5"/></svg>barrowdalepowerloft.com.au</div>
  </div>
</section>

<section class="flyer flyer--back">
  <div class="plate"></div>
  <div class="brand"><span class="brand-dot"></span>Barrowdale Power Loft</div>
  <h2 class="headline"><span class="headline-top">Health Through</span><span class="headline-main">Strength</span></h2>
  <p class="tagline">You don’t have to live in pain.</p>
  <div class="photo photo-knee" role="img" aria-label="Black and white photo of hands holding a knee, painful area glowing red"></div>
  <div class="body-copy">
    <p>Strength training has been shown to improve many chronic pain conditions and is now being routinely recommended by medical and health professionals.</p>
    <p>Our private studio provides high quality strength training by expert strength coaches. We’ve helped countless people improve or eliminate chronic pain, contact us today and find out how we can help you.</p>
  </div>
  <div class="phone">
    <svg viewBox="0 0 44 44"><circle cx="22" cy="22" r="20" fill="#fff" stroke="var(--red)" stroke-width="3"/><path d="M15 13c2-1 3 0 4 2l1 3c0 1-1 2-2 3 1 3 3 5 6 6 1-1 2-2 3-2l3 1c2 1 3 2 2 4-1 2-3 3-5 3-8-1-14-7-15-15 0-2 1-4 3-5z" fill="var(--red)"/></svg>
    <span>0452 918 064</span>
  </div>
  <div class="band">
    <div class="band-row"><svg viewBox="0 0 20 20"><path d="M10 1a6 6 0 0 1 6 6c0 5-6 12-6 12S4 12 4 7a6 6 0 0 1 6-6z" fill="none" stroke="#fff" stroke-width="2"/><circle cx="10" cy="7" r="2" fill="#fff"/></svg>4/83 Kinross Hill Rd, Barrowdale</div>
    <div class="band-row"><svg viewBox="0 0 20 20"><circle cx="10" cy="10" r="8" fill="none" stroke="#fff" stroke-width="2"/><path d="M2 10h16M10 2c3 3 3 13 0 16M10 2c-3 3-3 13 0 16" fill="none" stroke="#fff" stroke-width="1.5"/></svg>barrowdalepowerloft.com.au</div>
  </div>
</section>

</body>
</html>
```